Custom Monogramming and Retail gifts

We need a Business Card for a monogramming business that offers many retail gift options. We are a home based business that uses social media (Chatterbox,clipboardia and our website) to sell our products. Our target market is college age, high school, baby gifts.
We want a preppy fun look. Monogramming is very popular in the South

Industry/Entity Type

College

Contact Information for Business Card

Threadwell Keepsakes
Custom Monogramming and Gifts
7152 Brackenway Lane
Gainesville, GA 30999
Della Marsh, Owner
555-314-2790
threadwellkeepsakes.example
threadwellkeepsakes@mailbox.example

```html
<!DOCTYPE html>
<html lang="en">
<head>
<meta charset="utf-8">
<title>Threadwell Keepsakes – Business Card</title>
<link rel="stylesheet" href="https://fonts.googleapis.com/css2?family=Courgette&family=Noto+Sans:wght@400&family=Open+Sans:wght@400&display=swap">
<style>
  :root {
    --page: #ffffff;
    --card: #ffffff;
    --pink: #ec2fa8;
    --ink: #111111;
    --grey: #3f4448;
  }
  html, body {
    margin: 0;
    width: 1200px;
    height: 984px;
    overflow: hidden;
    background: var(--page);
  }
  .canvas {
    position: relative;
    width: 1200px;
    height: 984px;
  }
  .card {
    position: absolute;
    left: 218px;
    top: 322px;
    width: 726px;
    height: 424px;
    background: var(--card);
    box-shadow: 3px 5px 6px rgba(0,0,0,0.35);
    overflow: hidden;
  }
  .stripe-band {
    position: absolute;
  }
  .stripe-band--top,
  .stripe-band--bottom {
    left: 0;
    right: 0;
    height: 30px;
    background: repeating-linear-gradient(to bottom,
      var(--pink) 0 2px, #fff 2px 5px);
  }
  .stripe-band--top { top: 0; }
  .stripe-band--bottom { bottom: 0; }
  .stripe-band--left,
  .stripe-band--right {
    top: 0;
    bottom: 0;
    width: 28px;
    background: repeating-linear-gradient(to right,
      var(--pink) 0 2px, #fff 2px 5px);
    mix-blend-mode: multiply;
  }
  .stripe-band--left { left: 0; }
  .stripe-band--right { right: 0; }

  .brand-name {
    position: absolute;
    left: 60px;
    top: 150px;
    width: 290px;
    text-align: center;
    font-family: "Noto Sans", Verdana, sans-serif;
    font-size: 27px;
    line-height: 1.3;
    color: var(--ink);
  }
  .brand-dot {
    display: block;
    width: 14px;
    height: 14px;
    margin: 0 auto 10px;
    border-radius: 50%;
    background: var(--pink);
  }
  .website {
    position: absolute;
    left: 76px;
    top: 344px;
    font-family: "Open Sans", Arial, sans-serif;
    font-size: 16px;
    letter-spacing: 1px;
    color: var(--grey);
  }
  .headline {
    position: absolute;
    left: 398px;
    top: 78px;
    margin: 0;
    font-family: "Courgette", cursive;
    font-weight: 400;
    font-size: 23px;
    line-height: 31px;
    color: var(--ink);
  }
  .contact {
    position: absolute;
    left: 399px;
    font-family: "Noto Sans", Verdana, sans-serif;
    font-size: 13px;
    line-height: 17px;
    color: var(--ink);
    margin: 0;
  }
  .contact--phone { top: 253px; }
  .contact--address { top: 277px; }
  .contact--email { top: 348px; }
</style>
</head>
<body>
<div class="canvas">
  <section class="card">
    <div class="stripe-band stripe-band--top"></div>
    <div class="stripe-band stripe-band--bottom"></div>
    <div class="stripe-band stripe-band--left"></div>
    <div class="stripe-band stripe-band--right"></div>

    <div class="brand-name"><span class="brand-dot"></span>Threadwell Keepsakes</div>
    <div class="website">threadwellkeepsakes.example</div>

    <h1 class="headline">Threadwell Keepsakes<br>Custom Monogramming<br>and Gifts</h1>

    <p class="contact contact--phone">555-314-2790</p>
    <p class="contact contact--address">7152 Brackenway<br>Lane Gainesville, GA 30999<br>Della Marsh, Owner</p>
    <p class="contact contact--email">threadwellkeepsakes@mailbox.example</p>
  </section>
</div>
</body>
</html>
```